KPW Authorised Dealer needs Business Cards

We need a business card designed for our branch owners. Solvane Alarms is an Authorised KPW Dealer and does its own independent installations outside of the KPW work we perform so whilst the KPW Authorised Dealer Logo needs to be included, it should not be overwhelming in respect of the overall look of the card. I would like a rounded edge to the cards corners rather than a 90 degree hard edge. We also need to promote the fact that we do First Class Alarm & CCTV Solutions. (Details of card holder to follow)

```html
<!DOCTYPE html>
<html lang="en">
<head>
<meta charset="utf-8">
<title>Solvane Alarms – Business Cards</title>
<link rel="stylesheet" href="https://fonts.googleapis.com/css2?family=Montserrat:wght@400;500;700&display=swap">
<style>
  :root {
    --bg: #d9dadc;
    --brand-blue: #0f74c2;
    --brand-blue-light: #2b9ae6;
    --brand-blue-deep: #0a5aa5;
    --accent-yellow: #f6c416;
    --ink-dark: #3a3a3c;
    --paper: #ffffff;
    --text-font: "Montserrat", sans-serif;
  }
  * { margin: 0; padding: 0; box-sizing: border-box; }
  html, body {
    width: 1200px; height: 900px; overflow: hidden;
    background: var(--bg);
    font-family: var(--text-font);
  }
  .canvas { position: relative; width: 1200px; height: 900px; }

  .card {
    position: absolute; left: 300px;
    width: 600px; height: 340px;
    border-radius: 30px; overflow: hidden;
    box-shadow: 0 6px 18px rgba(0,0,0,0.18);
  }

  /* Front */
  .card-front { top: 90px; }
  .front-backdrop {
    position: absolute; inset: 0;
    background: linear-gradient(135deg, var(--brand-blue-light) 0%, var(--brand-blue) 50%, var(--brand-blue-deep) 100%);
  }
  .front-content {
    position: absolute; inset: 0;
    display: flex; flex-direction: column; align-items: center; justify-content: center;
    color: var(--paper);
  }
  .front-brand-mark {
    width: 40px; height: 40px; background: var(--paper); margin-bottom: 16px;
  }
  .front-brand-name {
    font-weight: 700; font-size: 40px; letter-spacing: 1px; line-height: 1;
  }
  .front-web { font-size: 14px; font-weight: 500; margin-top: 10px; }
  .front-tagline {
    margin-top: 14px; background: var(--accent-yellow); color: var(--ink-dark);
    font-size: 16px; font-weight: 500; padding: 6px 34px;
  }

  /* Back */
  .card-back { top: 470px; background: var(--paper); }
  .back-brand {
    position: absolute; left: 30px; top: 110px; width: 240px;
    display: flex; flex-direction: column; align-items: center; gap: 14px;
  }
  .back-brand-mark { width: 44px; height: 44px; background: var(--brand-blue); }
  .back-brand-name {
    font-weight: 700; font-size: 22px; line-height: 1;
    color: var(--brand-blue); letter-spacing: 0.5px; white-space: nowrap;
  }
  .contact-panel {
    position: absolute; left: 300px; top: 50px; width: 260px;
    background: var(--brand-blue); color: var(--paper);
    padding: 14px 18px;
  }
  .holder-name { font-weight: 700; font-size: 19px; letter-spacing: 0.5px; }
  .holder-title { font-size: 13px; margin: 2px 0 10px; }
  .contact-line { display: flex; align-items: center; gap: 8px; font-size: 14px; margin-top: 4px; white-space: nowrap; }
  .contact-icon {
    width: 16px; height: 16px; background: var(--accent-yellow);
    display: flex; align-items: center; justify-content: center; flex: none;
  }
  .web-band {
    position: absolute; left: 300px; top: 188px; width: 260px;
    background: var(--accent-yellow); color: var(--ink-dark);
    font-size: 15px; font-weight: 500; padding: 5px 18px;
  }
  .dealer-badge {
    position: absolute; left: 318px; top: 240px;
    width: 38px; height: 38px; border-radius: 50%;
    background: var(--brand-blue-deep);
  }
</style>
</head>
<body>
<main class="canvas">

  <section class="card card-front" aria-label="Business card front">
    <div class="front-backdrop" role="img" aria-label="Blue faceted geometric background"></div>
    <div class="front-content">
      <div class="front-brand-mark"></div>
      <div class="front-brand-name">SOLVANE ALARMS</div>
      <div class="front-web">www.solvanealarms.com</div>
      <div class="front-tagline">First Class Alarm &amp; CCTV Solutions</div>
    </div>
  </section>

  <section class="card card-back" aria-label="Business card back">
    <div class="back-brand">
      <div class="back-brand-mark"></div>
      <div class="back-brand-name">SOLVANE ALARMS</div>
    </div>

    <div class="contact-panel">
      <div class="holder-name">JOHNATHAN DOE</div>
      <div class="holder-title">Title</div>
      <div class="contact-line">
        <span class="contact-icon">
          <svg width="11" height="11" viewBox="0 0 24 24"><path fill="#0f74c2" d="M6.6 10.8a15.1 15.1 0 0 0 6.6 6.6l2.2-2.2a1 1 0 0 1 1-.25 11.4 11.4 0 0 0 3.6.57 1 1 0 0 1 1 1V20a1 1 0 0 1-1 1A17 17 0 0 1 3 4a1 1 0 0 1 1-1h3.5a1 1 0 0 1 1 1c0 1.25.2 2.45.57 3.57a1 1 0 0 1-.25 1z"/></svg>
        </span>
        <span>5550142873</span>
      </div>
      <div class="contact-line">
        <span class="contact-icon">
          <svg width="11" height="11" viewBox="0 0 24 24"><rect x="2" y="5" width="20" height="14" fill="none" stroke="#0f74c2" stroke-width="2.4"/><path d="M2 6l10 7 10-7" fill="none" stroke="#0f74c2" stroke-width="2.4"/></svg>
        </span>
        <span>info@solvanealarms.com</span>
      </div>
    </div>
    <div class="web-band">www.solvanealarms.com</div>
    <div class="dealer-badge" role="img" aria-label="KPW authorised dealer badge"></div>
  </section>

</main>
</body>
</html>
```